Template Flyer- Lunarcore Pilates & Yoga

I am wanting a template 1 page flyer designed to use on the back ground of newsletter (faded background) and for our advertising posters in A4, A3, for Facebook and Instagram compatibility.

I have loaded an example from another Studio called Fernbrook (file 3)- each time they have a new workshop to advertise a picture is placed in the little circle (so this is something I would want to do too where I can load a new picture each time a new workshop is running)- They have used the flyer like a water mark...I like this.

Our colour palette is what is on our logos and you can also visit our website for a feel for what we like www.lunarcorepilates.com.au

I need some of the designs edited a bit more and because of the time difference, there seems to be a 24hour period where we communicate with each other. May I please request another 2 days extension

Need extra days to review

Requirements
Must have
• Id like to have a picture in the back ground. My favourite back ground that has been produced so far is a background of both picture file 9 and 10 in either.
Nice to have
• 3 picture circles options to advertise the events/workshops I have each year.
• Brush stroke style circles (see picture attached)rather then smooth circles for the picture area (in a grey tone)
Should not have
• No BLACK colour writing or black circles

```html
<!DOCTYPE html>
<html lang="en">
<head>
<meta charset="utf-8">
<title>Pilates and Yoga Workshop – Lunarcore Pilates &amp; Yoga</title>
<link rel="stylesheet" href="https://fonts.googleapis.com/css2?family=Montserrat:wght@400;500;700&display=swap">
<style>
  :root {
    --cream-light: #fbf6ec;
    --cream: #f3e8d4;
    --cream-deep: #ead9bd;
    --teal: #1a8ea8;
    --stone: #a99f95;
    --crescent: #c9c0b7;
    --photo-dark: #1f140e;
    --photo-mid: #3b271b;
  }
  * { margin: 0; padding: 0; box-sizing: border-box; }
  html, body { width: 934px; height: 1200px; overflow: hidden; }
  body { font-family: "Montserrat", Arial, sans-serif; }

  .flyer {
    position: relative;
    width: 934px;
    height: 1200px;
    overflow: hidden;
    background:
      linear-gradient(90deg, var(--cream-light) 0%, var(--cream) 18%, var(--cream-light) 34%, var(--cream-deep) 52%, var(--cream-light) 68%, var(--cream) 84%, var(--cream-light) 100%);
  }

  .feature-art { position: absolute; left: 0; top: 0; width: 934px; height: 720px; }

  .event-title {
    position: absolute;
    top: 734px;
    left: 0;
    width: 934px;
    text-align: center;
    font-weight: 700;
    font-size: 48px;
    letter-spacing: -0.2px;
    color: var(--teal);
  }

  .event-details {
    position: absolute;
    top: 832px;
    left: 0;
    width: 934px;
    text-align: center;
    color: var(--teal);
    font-weight: 500;
  }
  .detail { font-size: 24px; line-height: 1; margin-bottom: 28px; }
  .detail-label { color: var(--stone); font-weight: 400; }
  .detail-cost { margin-bottom: 8px; }
  .price-note { font-size: 19px; }
  .price-second { font-size: 24px; line-height: 1; }

  .brand {
    position: absolute;
    right: 46px;
    bottom: 72px;
    display: flex;
    align-items: center;
    gap: 14px;
  }
  .brand-dot {
    width: 52px;
    height: 52px;
    border-radius: 50%;
    border: 3px solid var(--teal);
  }
  .brand-name {
    font-size: 32px;
    font-weight: 400;
    color: var(--teal);
    letter-spacing: -0.3px;
  }
</style>
</head>
<body>
<main class="flyer">
  <svg class="feature-art" viewBox="0 0 934 720" aria-hidden="false">
    <defs>
      <radialGradient id="photoTone" cx="50%" cy="50%" r="55%">
        <stop offset="0%" stop-color="#4a3122"/>
        <stop offset="60%" stop-color="var(--photo-mid)"/>
        <stop offset="100%" stop-color="var(--photo-dark)"/>
      </radialGradient>
    </defs>
    <path class="crescent-frame" fill="var(--crescent)" fill-rule="evenodd"
          d="M470 80 a306 306 0 1 0 0.1 0 Z M452 80 a290 290 0 1 0 0.1 0 Z"/>
    <g role="img" aria-label="Workshop photo: a circle of hands reaching inward on a dark timber floor, with small flowers in the centre">
      <circle class="workshop-photo" cx="446" cy="364" r="282" fill="url(#photoTone)"/>
    </g>
  </svg>

  <h1 class="event-title">Pilates and Yoga Workshop</h1>

  <section class="event-details">
    <p class="detail"><span class="detail-label">Where:</span> Lunarcore Pilates &amp; Yoga, Wattle Vale VIC</p>
    <p class="detail"><span class="detail-label">When:</span> Saturday, March 24th 10am - 4pm</p>
    <p class="detail detail-cost"><span class="detail-label">Cost:</span> $120 <span class="price-note">(non concession)</span></p>
    <p class="price-second">$100 <span class="price-note">(concession holders)</span></p>
  </section>

  <footer class="brand">
    <span class="brand-dot"></span>
    <span class="brand-name">lunarcore pilates &amp; yoga</span>
  </footer>
</main>
</body>
</html>
```